Landing page для Vorlan parts
Название сайта (домена, или проекта)
Vorlan parts
Укажите ссылки на сайты, которые нравятся
https://tulvek.ru/
Оптово-розничные покупатели оригинальных запчастей на автомобили. Средний чек от 30 000 рублей. Мужчины. Мы возим только оригинальные запчасти из Европы, у нас высокая скорость доставки! от 5 рабочих дней.
Этот сайт в принципе нравится https://dombrall.ru/?ysclid=pxbtr2wk7h318274609 ( не сама цветовая гамма) а расположение блоков.
У нас сайт создан на платформе MRTZ. Платформа предполагает использование шаблонных вариантов сайта, то есть сайт реализован на готовом шаблоне. Ниже мы прикладываем используемый шаблон.
https://vorlan-parts.ru/?templateId=31&class=301&color=206351
Важно учитывать, что выход за рамки возможностей шаблона невозможен. Поэтому макет дизайна лендинг-пейджа по техническому заданию, представленному ниже, необходимо разрабатывать строго с учётом функциональных и визуальных возможностей, которые предоставляет данный шаблон сайта.
https://files.kestroom.net/document/d/7Q_zrtk9LMw4PjuXbn2VcYoe8fHa3Gs1KtRnd0yLpEw/edit?tab=t.0
Адаптивность сайта
Десктопная версия, Версия для планшетов, Версия для телефонов

```html
<!DOCTYPE html>
<html lang="ru">
<head>
<meta charset="utf-8">
<title>Оригинальные автозапчасти из Европы</title>
<link rel="stylesheet" href="https://fonts.googleapis.com/css2?family=Oswald:wght@300;400;500&display=swap">
<style>
  :root {
    --bg-deep: #0b0b0c;
    --bg-mid: #1c1d1f;
    --smoke: #6d7074;
    --text: #ffffff;
    --accent: #8c1114;
    --accent-line: #9b1a1d;
  }
  * { margin: 0; padding: 0; box-sizing: border-box; }
  html, body {
    width: 883px;
    height: 1200px;
    overflow: hidden;
    background: var(--bg-deep);
  }
  .hero {
    position: relative;
    width: 883px;
    height: 1200px;
    overflow: hidden;
    font-family: "Oswald", sans-serif;
    color: var(--text);
  }
  .hero__backdrop {
    position: absolute;
    inset: 0;
    background:
      radial-gradient(ellipse 620px 260px at 50% 1040px, rgba(150,154,160,0.55), transparent 70%),
      radial-gradient(ellipse 520px 200px at 70% 880px, rgba(110,114,120,0.35), transparent 70%),
      radial-gradient(ellipse 700px 420px at 60% 300px, rgba(60,62,66,0.35), transparent 75%),
      linear-gradient(180deg, var(--bg-deep) 0%, var(--bg-mid) 55%, var(--smoke) 88%, #2a2b2d 100%);
  }
  .hero__car {
    position: absolute;
    left: 250px;
    top: 1140px;
    width: 720px;
    height: 120px;
    border-radius: 50% 50% 0 0 / 100% 100% 0 0;
    background: linear-gradient(180deg, #1a1b1d 0%, #0e0f10 100%);
  }
  .hero__content {
    position: relative;
    padding: 64px 36px 0;
  }
  .hero__title {
    font-weight: 500;
    font-size: 85px;
    line-height: 108px;
    letter-spacing: 0.5px;
    text-transform: uppercase;
  }
  .hero__subtitle {
    margin-top: 52px;
    font-weight: 500;
    font-size: 45px;
    line-height: 50px;
    text-transform: uppercase;
  }
  .hero__benefits {
    list-style: none;
    margin-top: 76px;
    font-weight: 300;
    font-size: 40px;
    line-height: 58px;
    text-transform: uppercase;
  }
  .hero__actions {
    position: absolute;
    left: 36px;
    top: 809px;
    width: 807px;
  }
  .btn {
    display: flex;
    align-items: center;
    justify-content: center;
    width: 100%;
    height: 112px;
    border-radius: 6px;
    font-family: "Oswald", sans-serif;
    font-weight: 400;
    font-size: 36px;
    text-transform: uppercase;
    color: var(--text);
  }
  .btn--primary { background: var(--accent); }
  .btn--outline {
    margin-top: 45px;
    background: transparent;
    border: 3px solid var(--accent-line);
  }
</style>
</head>
<body>
  <section class="hero">
    <div class="hero__backdrop" role="img" aria-label="Тёмный автосервис с дымом и силуэтом автомобиля внизу"></div>
    <div class="hero__car" role="img" aria-label="Силуэт автомобиля"></div>
    <div class="hero__content">
      <h1 class="hero__title">Оригинальные<br>автозапчасти<br>из Европы</h1>
      <p class="hero__subtitle">С доставкой от 3 рабочих дней</p>
      <ul class="hero__benefits">
        <li>100% оригинал</li>
        <li>Гарантия совместимости</li>
        <li>Без посредников</li>
      </ul>
    </div>
    <div class="hero__actions">
      <div class="btn btn--primary">Подобрать запчасти</div>
      <div class="btn btn--outline">Получить консультацию</div>
    </div>
  </section>
</body>
</html>
```